Bright Path Trading
Business Cards and Stationary
Project: Bright Path Trading
Bright Path Trading -
Creative Brief
Modern
Rob and Kara Halvorsen, Owners
47 Elmcrest Road Northampton, MA 01384
rob@brightpathtrading.com
www.brightpathtrading.com
Please put Kara's email underneath Rob's email: kara@brightpathtrading.com

```html
<!DOCTYPE html>
<html lang="en">
<head>
<meta charset="utf-8">
<title>Bright Path Trading – Business Card</title>
<link rel="stylesheet" href="https://fonts.googleapis.com/css2?family=Arimo:wght@400;700&display=swap">
<style>
  :root {
    --paper-light: #f4f4f4;
    --paper-mid: #dcdcdc;
    --wine-dark: #6e1f26;
    --wine: #8e3a40;
    --wine-light: #b0686b;
    --ink-brand: #3e2a22;
    --ink-light: #ffffff;
  }
  html, body {
    margin: 0;
    padding: 0;
    overflow: hidden;
    background: #ffffff;
  }
  .card {
    position: relative;
    width: 1200px;
    height: 686px;
    overflow: hidden;
    font-family: "Arimo", Arial, sans-serif;
  }
  .card-background {
    position: absolute;
    inset: 0;
    width: 1200px;
    height: 686px;
  }
  .brand {
    position: absolute;
    left: 560px;
    top: 178px;
    display: flex;
    align-items: center;
    gap: 18px;
  }
  .brand-dot {
    width: 34px;
    height: 34px;
    border-radius: 50%;
    background: var(--wine);
  }
  .brand-name {
    margin: 0;
    font-size: 54px;
    font-weight: 700;
    color: var(--ink-brand);
    letter-spacing: 0.5px;
    white-space: nowrap;
  }
  .address {
    position: absolute;
    left: 38px;
    top: 448px;
    margin: 0;
    font-style: normal;
    font-size: 29px;
    line-height: 37px;
    color: var(--ink-light);
    white-space: nowrap;
  }
  .address-indent {
    padding-left: 44px;
  }
  .owners {
    position: absolute;
    right: 30px;
    top: 566px;
    color: var(--ink-light);
    white-space: nowrap;
  }
  .owners-names {
    margin: 0;
    font-size: 29px;
    font-weight: 700;
    line-height: 38px;
  }
  .owners-role {
    margin: 0;
    font-size: 27px;
    line-height: 36px;
  }
</style>
</head>
<body>
  <div class="card">
    <svg class="card-background" viewBox="0 0 1200 686" xmlns="http://www.w3.org/2000/svg" aria-hidden="true">
      <defs>
        <radialGradient id="paperGlow" cx="0.6" cy="0.25" r="0.8">
          <stop offset="0" stop-color="#f4f4f4"/>
          <stop offset="1" stop-color="#dcdcdc"/>
        </radialGradient>
        <radialGradient id="wineGlow" cx="0.3" cy="0.75" r="0.9">
          <stop offset="0" stop-color="#b0686b"/>
          <stop offset="0.45" stop-color="#8e3a40"/>
          <stop offset="1" stop-color="#6e1f26"/>
        </radialGradient>
      </defs>
      <rect class="paper" width="1200" height="686" fill="url(#paperGlow)"/>
      <path class="wine-band" d="M0 0 H150 C 420 280, 800 520, 1200 612 V686 H0 Z" fill="url(#wineGlow)"/>
      <path class="wine-stripe" d="M0 40 C 300 200, 700 470, 1200 640" fill="none" stroke="#b0686b" stroke-opacity="0.35" stroke-width="10"/>
      <path class="wine-stripe" d="M60 0 C 340 240, 760 500, 1200 600" fill="none" stroke="#ffffff" stroke-opacity="0.18" stroke-width="4"/>
    </svg>

    <div class="brand">
      <span class="brand-dot"></span>
      <h1 class="brand-name">Bright Path Trading</h1>
    </div>

    <address class="address">
      47 Elmcrest Road Northampton,<br>
      MA 01384 Ph : 413.555.0142<br>
      F : 413.555.0143<br>
      E : rob@brightpathtrading.com<br>
      <span class="address-indent">kara@brightpathtrading.com</span><br>
      W: www.brightpathtrading.com
    </address>

    <div class="owners">
      <p class="owners-names">Rob and Kara Halvorsen</p>
      <p class="owners-role">Owners</p>
    </div>
  </div>
</body>
</html>
```